Business Card Design for Kidvale (Hires out childrens play areas)

Looking to have a business card designed for a company we just bought. The company rents out childrens play areas.

I have uploaded a couple of examples of the kind of business card style I like. Here are two more examples:

https://quorvastudio.nz/project/bright-romp-branding/
https://imgvaultcdn.com/design_img/8841052/302917/302917_5518203_8841052_b73e19a2_image.jpg

I think a white card will be best due to all the colours in the logo.

Size we require: 3.75" x 2.25" (horizontally orientated) with a 0.125" bleed

Uploaded is two versions of our logo.

Details for the card:
1. My name: Liam Verster
2. Title: Managing Director
3. Phone no: 021 563 417
4. Email: liam@kidvale.co.nz
5. URL: www.kidvale.co.nz
6. Address:
PO Box 318625
Fernlea, Auckland

Let me know if you need anything else.

Target Market(s)

Hospitals, doctors surgeries, bed shops, etc.

Contact Information for Business Card

Details for the card:
1. My name: Liam Verster
3. Phone no: 021 563 417
5. URL: www.kidvale.co.nz
6. Address:
PO Box 318625
Fernlea, Auckland

Requirements
Should not have
• Not too busy.

```html
<!DOCTYPE html>
<html lang="en">
<head>
<meta charset="utf-8">
<title>Kidvale — Business Card</title>
<link rel="stylesheet" href="https://fonts.googleapis.com/css2?family=Quicksand:wght@500;600;700&display=swap">
<style>
  :root {
    --brand-blue: #1f5ca8;
    --brand-blue-deep: #184b8c;
    --accent-orange: #e8901e;
    --ink: #1e1e1e;
    --paper: #ffffff;
    --backdrop: #3b4048;
    --icon-teal: #1a9ea3;
    --icon-red: #d52b35;
    --icon-green: #2f9e46;
    --logo-dot: #f4a51c;
  }
  * { box-sizing: border-box; margin: 0; padding: 0; }
  html, body {
    width: 1200px; height: 800px; overflow: hidden;
    background: var(--backdrop);
    font-family: "Quicksand", "Century Gothic", sans-serif;
  }
  .canvas { position: relative; width: 1200px; height: 800px; }

  .card {
    position: absolute;
    width: 560px; height: 336px;
    border-radius: 4px;
    overflow: hidden;
    box-shadow: 0 14px 30px rgba(0,0,0,0.35);
  }

  /* Brand lockup */
  .brand {
    display: flex; align-items: center; gap: 12px;
    color: var(--paper);
    font-weight: 700;
    letter-spacing: 0.5px;
  }
  .brand-dot {
    border-radius: 50%;
    background: var(--logo-dot);
    flex: none;
  }

  /* Card back: blue with centred brand */
  .card-back {
    left: 110px; top: 44px;
    background: var(--brand-blue);
    display: flex; align-items: center; justify-content: center;
  }
  .card-back .brand { font-size: 64px; }
  .card-back .brand-dot { width: 44px; height: 44px; }

  /* Card front: white with blue curved panel */
  .card-front {
    left: 530px; top: 420px;
    background: var(--paper);
  }
  .card-front .panel {
    position: absolute; inset: 0;
    width: 560px; height: 336px;
  }
  .card-front .panel-brand {
    position: absolute; left: 345px; top: 96px; width: 190px;
    display: flex; flex-direction: column; align-items: center;
  }
  .card-front .panel-brand .brand { font-size: 40px; gap: 8px; }
  .card-front .panel-brand .brand-dot { width: 26px; height: 26px; }
  .address {
    margin-top: 26px;
    color: var(--paper);
    font-size: 13px; font-weight: 500;
    line-height: 1.35;
    text-align: center;
  }

  .person { position: absolute; left: 44px; top: 92px; }
  .person-name {
    color: var(--accent-orange);
    font-size: 30px; font-weight: 700;
    letter-spacing: 0.3px;
    text-transform: uppercase;
    line-height: 1;
  }
  .person-title {
    color: var(--ink);
    font-size: 19px; font-weight: 600;
    margin-top: 4px;
  }

  .contacts { position: absolute; left: 44px; top: 190px; list-style: none; }
  .contact {
    display: flex; align-items: center; gap: 12px;
    color: var(--ink);
    font-size: 16px; font-weight: 600;
    height: 30px; margin-bottom: 6px;
  }
  .contact-icon {
    width: 28px; height: 28px; border-radius: 5px;
    display: flex; align-items: center; justify-content: center;
    flex: none;
  }
  .contact-icon.phone { background: var(--icon-teal); }
  .contact-icon.email { background: var(--icon-red); }
  .contact-icon.web { background: var(--icon-green); }
  .contact-icon svg { width: 16px; height: 16px; }
</style>
</head>
<body>
<main class="canvas">

  <section class="card card-back" aria-label="Business card back">
    <div class="brand"><span class="brand-dot"></span>Kidvale</div>
  </section>

  <section class="card card-front" aria-label="Business card front">
    <svg class="panel" viewBox="0 0 560 336" aria-hidden="true">
      <defs>
        <filter id="panel-shadow" x="-20%" y="-20%" width="140%" height="140%">
          <feDropShadow dx="-3" dy="2" stdDeviation="5" flood-color="#000" flood-opacity="0.3"/>
        </filter>
      </defs>
      <path d="M372 0 C 268 96, 300 282, 470 336 L560 336 L560 0 Z"
            fill="var(--brand-blue)" filter="url(#panel-shadow)"/>
    </svg>

    <div class="person">
      <h1 class="person-name">Liam Verster</h1>
      <p class="person-title">Managing Director</p>
    </div>

    <ul class="contacts">
      <li class="contact">
        <span class="contact-icon phone">
          <svg viewBox="0 0 24 24" fill="none" stroke="#fff" stroke-width="2" stroke-linecap="round" stroke-linejoin="round">
            <path d="M5 3h4l2 5-2.5 1.5a11 11 0 0 0 6 6L16 13l5 2v4a2 2 0 0 1-2 2A16 16 0 0 1 3 5a2 2 0 0 1 2-2z"/>
          </svg>
        </span>
        021 563 417
      </li>
      <li class="contact">
        <span class="contact-icon email">
          <svg viewBox="0 0 24 24" fill="none" stroke="#fff" stroke-width="2" stroke-linejoin="round">
            <rect x="3" y="5" width="18" height="14" rx="1"/>
            <path d="M3 6l9 7 9-7"/>
          </svg>
        </span>
        liam@kidvale.co.nz
      </li>
      <li class="contact">
        <span class="contact-icon web">
          <svg viewBox="0 0 24 24" fill="none" stroke="#fff" stroke-width="2">
            <circle cx="12" cy="12" r="9"/>
            <path d="M3 12h18M12 3c3 3 3 15 0 18M12 3c-3 3-3 15 0 18"/>
          </svg>
        </span>
        www.kidvale.co.nz
      </li>
    </ul>

    <div class="panel-brand">
      <div class="brand"><span class="brand-dot"></span>Kidvale</div>
      <p class="address">PO Box 318625<br>Fernlea, Auckland</p>
    </div>
  </section>

</main>
</body>
</html>
```